Thank you for shopping with us business card

We would like a thank you card for our rebranded business. We used to be "Brindle Goods" but are now "Marlow Finds. Old thank you card and new logo will be attached for reference. New thank you card does not have to be same design as old thank you card, but please use new logo.
Shopmart URL is now marlowfinds.shopmart.example
Instagram is @Marlow_Finds
Email is marlowfinds@mailbox.example
Thank you!

Contact Information for Business Card

Shopmart site, email, Instagram

```html
<!DOCTYPE html>
<html lang="en">
<head>
<meta charset="utf-8">
<title>Marlow Finds – Thank You Card</title>
<link rel="stylesheet" href="https://fonts.googleapis.com/css2?family=Montserrat:wght@500;900&family=Tinos:wght@400;700&display=swap">
<style>
  :root {
    --backdrop: #3a3a3a;
    --card-black: #050505;
    --card-white: #ffffff;
    --ink: #111111;
    --light: #ffffff;
  }
  * { box-sizing: border-box; margin: 0; padding: 0; }
  html, body { width: 1200px; height: 689px; overflow: hidden; }
  body {
    background: var(--backdrop);
    display: flex;
    align-items: center;
    justify-content: center;
    gap: 60px;
    font-family: "Tinos", "Times New Roman", serif;
  }
  .card {
    width: 520px;
    height: 297px;
    border-radius: 18px;
    overflow: hidden;
    box-shadow: 0 14px 30px rgba(0,0,0,0.45);
  }

  /* Front */
  .card-front {
    background: var(--card-black);
    display: flex;
    align-items: center;
    justify-content: center;
    gap: 22px;
  }
  .brand-mark {
    width: 58px;
    height: 58px;
    border-radius: 50%;
    background: var(--light);
  }
  .brand-divider {
    width: 2px;
    height: 96px;
    background: var(--light);
  }
  .brand-name {
    font-family: "Montserrat", Arial, sans-serif;
    font-weight: 500;
    font-size: 30px;
    line-height: 1.1;
    letter-spacing: 1px;
    text-transform: uppercase;
    color: var(--light);
  }

  /* Back */
  .card-back {
    background: var(--card-white);
    display: flex;
    flex-direction: column;
  }
  .thanks-band {
    background: var(--card-black);
    height: 140px;
    display: flex;
    align-items: center;
    justify-content: center;
    position: relative;
  }
  .thanks-heading {
    font-family: "Montserrat", Arial, sans-serif;
    font-weight: 900;
    font-size: 29px;
    line-height: 1.15;
    text-align: center;
    text-transform: uppercase;
    color: var(--light);
    margin-top: -14px;
  }
  .band-marker {
    position: absolute;
    left: 50%;
    bottom: -11px;
    width: 22px;
    height: 22px;
    margin-left: -11px;
    border-radius: 50%;
    background: var(--card-black);
  }
  .thanks-message {
    margin-top: 22px;
    font-weight: 700;
    font-size: 15px;
    line-height: 1.3;
    text-align: center;
    color: var(--ink);
  }
  .contact-list {
    list-style: none;
    display: flex;
    justify-content: space-around;
    padding: 0 14px;
    margin-top: 22px;
  }
  .contact-item {
    display: flex;
    flex-direction: column;
    align-items: center;
    gap: 6px;
    font-size: 12px;
    color: var(--ink);
  }
  .contact-icon {
    width: 26px;
    height: 26px;
    border: 1.5px solid var(--ink);
    border-radius: 50%;
    display: flex;
    align-items: center;
    justify-content: center;
  }
  .contact-icon svg { width: 14px; height: 14px; }
</style>
</head>
<body>

  <section class="card card-front">
    <div class="brand-mark"></div>
    <div class="brand-divider"></div>
    <h1 class="brand-name">Marlow<br>Finds</h1>
  </section>

  <section class="card card-back">
    <header class="thanks-band">
      <h2 class="thanks-heading">Thank you<br>for your purchase!</h2>
      <span class="band-marker"></span>
    </header>

    <p class="thanks-message">Your purchase made my day and I hope this package brightens yours.<br>Please come back and leave a review!</p>

    <ul class="contact-list">
      <li class="contact-item">
        <span class="contact-icon">
          <svg viewBox="0 0 16 16" fill="none" stroke="#111" stroke-width="1.3">
            <circle cx="8" cy="8" r="6.5"/>
            <ellipse cx="8" cy="8" rx="2.8" ry="6.5"/>
            <line x1="1.5" y1="8" x2="14.5" y2="8"/>
            <line x1="2.5" y1="4.8" x2="13.5" y2="4.8"/>
            <line x1="2.5" y1="11.2" x2="13.5" y2="11.2"/>
          </svg>
        </span>
        <span class="contact-text">marlowfinds.shopmart.example</span>
      </li>
      <li class="contact-item">
        <span class="contact-icon"></span>
        <span class="contact-text">@Marlow_Finds</span>
      </li>
      <li class="contact-item">
        <span class="contact-icon">
          <svg viewBox="0 0 16 16">
            <rect x="1.5" y="3.5" width="13" height="9" fill="#111"/>
            <polyline points="1.5,3.5 8,9 14.5,3.5" fill="none" stroke="#fff" stroke-width="1.2"/>
          </svg>
        </span>
        <span class="contact-text">marlowfinds@mailbox.example</span>
      </li>
    </ul>
  </section>

</body>
</html>
```